Cleaning services Business Card Design

I need a business card design for my Cleaning business. I would like perhaps emphasis on the company name, Muddle to Marvel. Maybe the Muddle would to dirty and the marvel would have sprinkles.

Industry/Entity Type

Business

Contact Information for Business Card

Muddle to Marvel Cleaning Services, Teodoro Perlas, Industrial, Commercial, & Residential 418-635-0247

```html
<!DOCTYPE html>
<html lang="en">
<head>
<meta charset="utf-8">
<title>Muddle to Marvel Cleaning Services — Business Card</title>
<link href="https://fonts.googleapis.com/css2?family=Lato:wght@300;400;700&display=swap" rel="stylesheet">
<style>
  :root {
    --backdrop: #d9d6d1;
    --card: #0b0b0b;
    --ink-white: #f2f2f2;
    --ink-soft: #bdbdbd;
    --ink-grey: #8e8e8e;
  }
  html, body {
    margin: 0;
    padding: 0;
    width: 1200px;
    height: 1023px;
    overflow: hidden;
    background: var(--backdrop);
  }
  .stage {
    width: 1200px;
    height: 1023px;
    display: flex;
    align-items: center;
    justify-content: center;
  }
  .business-card {
    position: relative;
    width: 875px;
    height: 500px;
    background: var(--card);
    border-radius: 6px;
    box-shadow: 0 18px 40px rgba(0,0,0,0.25);
    font-family: "Lato", Arial, sans-serif;
    color: var(--ink-white);
    overflow: hidden;
  }
  .brand {
    position: absolute;
    left: 70px;
    top: 150px;
    width: 340px;
  }
  .brand-name {
    margin: 0;
    font-size: 56px;
    font-weight: 700;
    letter-spacing: 3px;
    line-height: 1.05;
    text-transform: uppercase;
    color: var(--ink-soft);
  }
  .brand-line {
    display: block;
  }
  .brand-tagline {
    margin: 16px 0 0;
    font-size: 34px;
    font-weight: 300;
    color: var(--ink-white);
    white-space: nowrap;
  }
  .contact {
    position: absolute;
    left: 470px;
    top: 70px;
  }
  .contact-name {
    margin: 0;
    font-size: 38px;
    font-weight: 400;
    white-space: nowrap;
  }
  .contact-phone {
    margin: 6px 0 0;
    font-size: 34px;
    font-weight: 300;
    letter-spacing: 1px;
    white-space: nowrap;
  }
  .services {
    position: absolute;
    left: 70px;
    right: 70px;
    bottom: 50px;
    display: flex;
    justify-content: space-between;
    margin: 0;
    padding: 0;
    list-style: none;
  }
  .service {
    font-size: 24px;
    font-weight: 300;
    color: var(--ink-soft);
  }
</style>
</head>
<body>
  <main class="stage">
    <section class="business-card" aria-label="Business card">
      <div class="brand">
        <h1 class="brand-name"><span class="brand-line">Muddle to</span><span class="brand-line">Marvel</span></h1>
        <p class="brand-tagline">Cleaning Services</p>
      </div>
      <div class="contact">
        <p class="contact-name">Teodoro Perlas</p>
        <p class="contact-phone">418-635-0247</p>
      </div>
      <ul class="services">
        <li class="service">Residential</li>
        <li class="service">Commercial</li>
        <li class="service">Industrial</li>
      </ul>
    </section>
  </main>
</body>
</html>
```